Website for Brivex Partners

We need to create a website for our company. Attached is the site map of the website and data input needed. Our theme colour is RED and our Logo is attached

We need a very attractive design where graphics are largely used like flash.

The main idea of the website is to show Telecommunications Suppliers World Wide that we could assist them in getting more business in Africa and Middle East through our local presence in this region.
Updates

Target Market(s)

Telecommunication Suppliers and Clients

Industry/Entity Type

Business

Font styles to use
Serif
Sans Serif

Colors
ec2027

Requirements
Must have
• Graphics that shows Telecommunications Suppliers World Wide that we could assist them in getting more business in Africa and Middle East through our local presence in this region.

The website should be easy to edit for future changes by us.
Nice to have
• New ideas

```html
<!DOCTYPE html>
<html lang="en">
<head>
<meta charset="utf-8">
<title>Brivex Partners</title>
<link rel="stylesheet" href="https://fonts.googleapis.com/css2?family=Noto+Serif:wght@400;700&family=Open+Sans:ital,wght@0,400;0,600;1,400&display=swap">
<style>
:root{
  --brand-red:#c8161d;
  --ink:#333;
  --muted:#666;
  --line:#dcdcdc;
  --card-bg:#fafafa;
  --nav-top:#8a8a8a;
  --nav-bottom:#6b6b6b;
  --footer-bg:#3a3a3a;
  --footer-text:#e6e6e6;
  --icon:#555;
}
*{box-sizing:border-box;margin:0;padding:0}
html,body{width:1086px;height:1200px;overflow:hidden;background:#fff}
body{position:relative;font-family:"Open Sans",sans-serif;color:var(--ink)}
.abs{position:absolute}

.site-header{left:0;top:0;width:1086px;height:85px;background:#fff}
.brand{left:120px;top:30px;display:flex;align-items:center;gap:10px}
.brand-mark{width:26px;height:26px;background:var(--brand-red)}
.brand-name{font-family:"Open Sans",sans-serif;font-weight:600;font-size:24px;color:#555;letter-spacing:.5px;line-height:1}
.search{left:750px;top:29px;width:216px;height:32px;border:1px solid #d0d0d0;border-radius:2px;background:#fff}
.search span{position:absolute;left:14px;top:9px;font-size:10px;font-style:italic;color:#999}
.search svg{position:absolute;right:10px;top:7px}

.main-nav{left:0;top:85px;width:1086px;height:41px;background:linear-gradient(var(--nav-top),var(--nav-bottom))}
.main-nav a{position:absolute;top:0;height:41px;line-height:41px;font-family:"Noto Serif",serif;font-size:11px;color:#fff;text-decoration:none;transform:translateX(-50%);white-space:nowrap}
.main-nav a.active{background:var(--brand-red);width:83px;text-align:center}

.hero{left:0;top:126px;width:1086px;height:388px;background:linear-gradient(90deg,#8a8580 0%,#d8d2cc 35%,#efece8 60%,#d9d6d2 85%,#c9c6c2 100%)}
.hero-caption{left:548px;top:230px;width:374px;height:183px;background:rgba(255,255,255,.82)}
.hero-title{left:17px;top:22px;font-family:"Noto Serif",serif;font-size:28px;color:var(--brand-red);line-height:1}
.hero-sub{left:17px;top:58px;font-family:"Noto Serif",serif;font-size:22px;color:#333;line-height:1}
.hero-text{left:18px;top:100px;width:345px;font-size:11.5px;line-height:20px;color:#444}
.hero-arrow{top:298px;width:46px;height:46px;border-radius:50%;background:rgba(90,90,90,.75)}
.hero-arrow svg{position:absolute;left:13px;top:13px}

.service{top:570px;width:200px;height:156px;border:1px solid var(--line);background:var(--card-bg);text-align:center}
.service svg{position:absolute;left:50%;top:16px;transform:translateX(-50%)}
.service h3{position:absolute;left:0;width:100%;top:94px;font-family:"Noto Serif",serif;font-weight:400;font-size:17px;line-height:22px;color:var(--brand-red)}
.service-next{left:987px;top:638px}

.info-card{top:762px;width:273px;height:282px;border:1px solid var(--line);background:var(--card-bg)}
.info-media{position:absolute;left:14px;top:14px;width:244px;height:128px}
.info-card h2{position:absolute;left:15px;top:159px;font-family:"Noto Serif",serif;font-weight:400;font-size:17px;color:var(--brand-red)}
.info-card p{position:absolute;left:15px;top:192px;width:245px;font-size:11px;line-height:18px;color:var(--muted)}
.read-more{font-style:italic;color:var(--brand-red)}

.site-footer{left:0;top:1093px;width:1086px;height:107px;background:var(--footer-bg)}
.social{top:24px;width:25px;height:25px;border-radius:50%;background:#cfcfcf}
.copyright{left:121px;top:70px;font-size:12px;color:var(--footer-text)}
.contact-title{left:778px;top:17px;font-family:"Noto Serif",serif;font-size:15px;color:#fff;display:flex;align-items:center;gap:7px}
.contact-line{left:778px;font-size:11px;color:var(--footer-text)}
</style>
</head>
<body>

<header class="site-header abs">
  <div class="brand abs"><span class="brand-mark"></span><span class="brand-name">BRIVEX PARTNERS</span></div>
  <div class="search abs"><span>Search here...</span>
    <svg width="20" height="18" viewBox="0 0 20 18"><circle cx="7" cy="7" r="5" fill="none" stroke="#555" stroke-width="2"/><line x1="11" y1="11" x2="18" y2="16" stroke="#555" stroke-width="3" stroke-linecap="round"/></svg>
  </div>
</header>

<nav class="main-nav abs">
  <a class="active" style="left:162px">HOME</a>
  <a style="left:278px">ABOUT US</a>
  <a style="left:391px">SERVICES</a>
  <a style="left:495px">GALLERY</a>
  <a style="left:589px">BLOG</a>
  <a style="left:695px">TESTIMONIALS</a>
  <a style="left:820px">CONTACT US</a>
</nav>

<section class="hero abs" role="img" aria-label="Smiling businessman in a grey suit talking on a mobile phone in a bright office"></section>
<div class="hero-arrow abs" style="left:94px"><svg width="20" height="20" viewBox="0 0 20 20"><polyline points="13,2 5,10 13,18" fill="none" stroke="#fff" stroke-width="1.5"/></svg></div>
<div class="hero-arrow abs" style="left:948px"><svg width="20" height="20" viewBox="0 0 20 20"><polyline points="7,2 15,10 7,18" fill="none" stroke="#fff" stroke-width="1.5"/></svg></div>
<div class="hero-caption abs">
  <div class="hero-title abs">TELECOMMUNICATION</div>
  <div class="hero-sub abs">SOLUTION PROVIDER</div>
  <p class="hero-text abs">Lorem ipsum dolor sit amet, consectetur adipisicing elit, sed do eiusmod tempor incididunt ut labore et dolore magna aliqua. Ut enim ad minim veniam, quis nostrud exercitation</p>
</div>

<div class="service abs" style="left:117px">
  <svg width="64" height="64" viewBox="0 0 64 64" fill="none" stroke="var(--icon)" stroke-width="3"><circle cx="32" cy="33" r="27"/><ellipse cx="32" cy="33" rx="12" ry="27"/><line x1="5" y1="33" x2="59" y2="33"/><line x1="32" y1="6" x2="32" y2="60"/><path d="M9 20h46M9 46h46"/><circle cx="16" cy="14" r="7" fill="var(--icon)" stroke="#fff" stroke-width="2"/></svg>
  <h3>Access Network<br>Solutions</h3>
</div>
<div class="service abs" style="left:334px">
  <svg width="64" height="64" viewBox="0 0 64 64"><path d="M10 20 L40 50 A22 22 0 0 1 10 20Z" fill="var(--icon)"/><line x1="25" y1="35" x2="40" y2="22" stroke="var(--icon)" stroke-width="3"/><circle cx="41" cy="21" r="3" fill="var(--icon)"/><path d="M44 12a10 10 0 0 1 8 8M46 5a17 17 0 0 1 13 13" fill="none" stroke="var(--icon)" stroke-width="3"/><path d="M20 44 L12 56 H34 L30 48Z" fill="var(--icon)"/></svg>
  <h3>Transmission Network<br>Solutions</h3>
</div>
<div class="service abs" style="left:551px">
  <svg width="84" height="64" viewBox="0 0 84 64" fill="none" stroke="var(--icon)" stroke-width="3"><circle cx="26" cy="30" r="24"/><ellipse cx="26" cy="30" rx="10" ry="24"/><line x1="2" y1="30" x2="50" y2="30"/><path d="M5 18h42M5 42h42"/><circle cx="46" cy="28" r="12" fill="#fafafa"/><line x1="55" y1="37" x2="78" y2="54" stroke-width="7" stroke-linecap="round"/></svg>
  <h3>Core Network<br>Solutions</h3>
</div>
<div class="service abs" style="left:768px">
  <svg width="68" height="68" viewBox="0 0 68 68"><g fill="var(--icon)"><circle cx="34" cy="34" r="22"/><g id="t"><rect x="29" y="4" width="10" height="12"/></g><use href="#t" transform="rotate(45 34 34)"/><use href="#t" transform="rotate(90 34 34)"/><use href="#t" transform="rotate(135 34 34)"/><use href="#t" transform="rotate(180 34 34)"/><use href="#t" transform="rotate(225 34 34)"/><use href="#t" transform="rotate(270 34 34)"/><use href="#t" transform="rotate(315 34 34)"/></g><circle cx="34" cy="34" r="13" fill="#fafafa"/></svg>
  <h3 style="top:96px">Value Added<br>Services</h3>
</div>
<svg class="service-next abs" width="24" height="24" viewBox="0 0 24 24"><circle cx="12" cy="12" r="11" fill="#fff" stroke="#888" stroke-width="1.5"/><path d="M9 6 L17 12 L9 18Z" fill="none" stroke="#888" stroke-width="1.5"/></svg>

<article class="info-card abs" style="left:117px">
  <div class="info-media" role="img" aria-label="Smiling businessman in front of a team of colleagues" style="background:linear-gradient(90deg,#5a5f6a,#8b7d73 50%,#d9dde2)"></div>
  <h2>About Us</h2>
  <p>Brivex Partners is a leading telecommunication Solution Provider; The company provides state of the art technologies and turnkey solutions to its clients that fully support. <span class="read-more">Read More &gt;&gt;</span></p>
</article>
<article class="info-card abs" style="left:406px">
  <div class="info-media" role="img" aria-label="People holding up cards printed with question marks" style="background:linear-gradient(180deg,#e4e4e4,#c9cdd3 70%,#4f86b8)"></div>
  <h2>Who We Are</h2>
  <p>Brivex Partners is a leading telecommunication Solution Provider; the company provides state of the art technologies and turnkey solutions.<br><span class="read-more">Read More &gt;&gt;</span></p>
</article>
<article class="info-card abs" style="left:696px">
  <div class="info-media" role="img" aria-label="Map of the region with red location pins marking offices" style="background:linear-gradient(135deg,#cfcfcf,#e6e6e6)"></div>
  <h2>We Serve you Everywhere</h2>
  <p>Our Head office in UK and we cover Middle East and Africa thorough a large and strong group of local footprint.</p>
</article>

<footer class="site-footer abs">
  <span class="social abs" style="left:121px"></span>
  <span class="social abs" style="left:152px"></span>
  <span class="social abs" style="left:183px"></span>
  <span class="social abs" style="left:213px"></span>
  <div class="copyright abs">Copyright © 2014 Brivex Partners. All rights reserved.</div>
  <div class="contact-title abs"><svg width="11" height="15" viewBox="0 0 11 15"><path d="M5.5 0A5.5 5.5 0 0 0 0 5.5C0 9.5 5.5 15 5.5 15S11 9.5 11 5.5A5.5 5.5 0 0 0 5.5 0Z" fill="#ddd"/><circle cx="5.5" cy="5.5" r="2" fill="var(--footer-bg)"/></svg>Contact Us</div>
  <div class="contact-line abs" style="top:57px">Street No. Building No., City, Zip code</div>
  <div class="contact-line abs" style="top:79px">Email : info@brivex-partners.com</div>
</footer>

</body>
</html>
```